Computer consultant website

Vexlo Software is a newly started computer consulting company. It's a small one-man company that provides mostly Android applications but also websites in collaboration with designers. I'm running this company on the side of full time university studies.

I'm in need of a website which will function as:
Primarily - I'll direct potential clients to the page so they can read about the company, what i offer and past work.
Secondarily - Making my company visible through the web and maybe getting new clients.

The final design should look modern, clean and professional.

Pages that will be in the final website are (Note that it's not the exact titles as the page will not be in english):
* About
* Services (what Vexlo offers)
* Portfolio/work
* Short news (like PlanHives "News and press")
* Contact.

Inspiration
http://www.planhive.example/design/87836
http://www.brambleorb.example/
http://www.planhive.example/design/845881
http://www.planhive.example/design/1369424 - Lighter design, however a bit cluttered.

No programming code is needed delivered at all. Focus on designing rather then coding.

If you have any questions, do not hesitate to send me a message.

Target Market(s)

Non-technical entrepreneurs and small companies.

Industry/Entity Type

University

Requirements
Must have
• Must have my company logo (see attachment).

Must in any way use both colors from my logo.

A way to logically rearrange content to fit smaller screens. I will implement this design so that it can be pleasantly viewed on mobile devices. You don't necessarily need to provide exactly how the design would look on mobile devices.

I need the following types of page designs:
* Landing page
* Content page
* Portfolio/work (with accompanying inside/clicked) page

Landing/start page must in any way include at least the information:
* Shorter version of "About Vexlo"
* At least 1 most recent portfolio/work entry
* At least 1 most recent news entry
* Services that Vexlo offers.
Nice to have
Should not have
• Testimonials or newsletter.

```html
<!DOCTYPE html>
<html lang="en">
<head>
<meta charset="utf-8">
<title>Vexlo Software</title>
<link rel="stylesheet" href="https://fonts.googleapis.com/css2?family=Arimo:wght@400;700&family=Varela+Round&display=swap">
<style>
:root{
  --blue:#2a7de1;
  --blue-soft:#78a6e4;
  --link:#2f76d2;
  --ink:#2b2b2b;
  --text:#555;
  --hero-dark:#2e2c2c;
  --hero-mid:#4a4848;
  --btn:#5a5a5a;
  --footer:#f1f1f1;
  --bar:#2d2d2d;
  --rule:#dcdcdc;
}
*{box-sizing:border-box;margin:0;padding:0}
html,body{width:986px;height:1200px;overflow:hidden}
body{position:relative;background:#fff;font-family:Arimo,Arial,sans-serif;color:var(--text)}
.abs{position:absolute}
.topline{left:0;top:0;width:986px;height:3px;background:var(--blue)}
.header{left:0;top:3px;width:986px;height:97px;background:linear-gradient(#fff 60%,#edf3fc)}
.brand{left:74px;top:24px;display:flex;align-items:center;gap:12px}
.brand-dot{width:56px;height:56px;border-radius:50%;background:var(--blue)}
.brand-name{font-family:"Varela Round",sans-serif;font-size:46px;color:var(--ink);line-height:1}
.nav{left:467px;top:45px;display:flex;gap:0;font-size:13px;font-weight:700;color:var(--ink)}
.nav a{display:block;padding:7px 12px;margin-right:9px;color:inherit;text-decoration:none;height:26px}
.nav a.active{background:#4a8fe8;color:#fff;border-radius:2px}
.hero{left:0;top:100px;width:986px;height:377px;background:radial-gradient(ellipse at 40% 45%,#5a5858,var(--hero-dark) 70%)}
.hero-art{left:75px;top:28px;width:310px;height:345px;border-radius:6px;background:linear-gradient(90deg,#e9e9e9,#cfd4d8 40%,#6f8a3d 85%,#3a3838)}
.hero h1{left:548px;top:84px;font-size:20px;font-weight:700;color:var(--blue-soft);letter-spacing:.5px}
.hero .rule{left:546px;width:367px;height:1px;background:#575555}
.hero p{left:546px;top:132px;width:367px;font-size:12px;line-height:19px;color:#cfcfcf;text-align:justify}
.pill{left:547px;top:261px;width:92px;height:26px;border-radius:13px;background:#fff;color:#555;font-size:12.5px;font-weight:700;text-align:center;line-height:26px}
.arrows{left:880px;top:337px;display:flex;gap:3px}
.arrows span{width:15px;height:18px;background:#777;border-radius:9px;display:flex;align-items:center;justify-content:center}
.about{left:0;top:477px;width:986px;height:180px;background:linear-gradient(#edf3fc,#fff 45px)}
.about h2{left:75px;top:28px;font-size:21px;font-weight:700;color:var(--blue)}
.about p{left:75px;top:60px;width:570px;font-size:12px;line-height:19px}
.frame{border:1px solid #ddd;padding:4px;background:#fff}
.frame div{width:100%;height:100%}
.about .frame{left:660px;top:29px;width:253px;height:118px}
.divider{left:75px;top:656px;width:838px;height:1px;background:linear-gradient(90deg,#e4e4e4,#e4e4e4 85%,transparent)}
.col{top:680px;width:252px}
.col h3{font-size:15.5px;font-weight:700;color:var(--blue);height:22px}
.col .go{position:absolute;right:0;top:0;width:16px;height:16px;border-radius:50%;background:#777}
.col .frame{width:252px;height:121px;margin-top:10px}
.col p{margin-top:10px;font-size:12px;line-height:19px;color:#444}
.btn{display:inline-block;width:70px;height:26px;background:var(--btn);color:#f2f2f2;font-size:12px;text-align:center;line-height:26px;border-radius:2px}
.services{list-style:none;border-top:1px solid var(--rule);margin-top:8px;padding-top:10px}
.services li{height:25.7px;font-size:12.5px;color:var(--link);display:flex;align-items:center;gap:10px}
.footer{left:0;top:951px;width:986px;height:200px;background:var(--footer);border-top:2px solid #e2e2e2}
.footer h4{font-size:15px;font-weight:400;color:var(--link)}
.links{list-style:none;top:52px;font-size:11px;color:#555}
.links li{height:24px}
.links li::before{content:"•";margin-right:6px;color:#888}
.social{left:743px;top:44px;list-style:none;font-size:11px;color:#555}
.social li{height:34px;display:flex;align-items:center;gap:16px}
.social i{width:23px;height:23px;background:#3b6aa8;display:block}
.social b{font-weight:400;font-size:12.5px;color:var(--link);margin-left:4px}
.bar{left:0;top:1151px;width:986px;height:49px;background:var(--bar)}
.bar p{left:74px;top:19px;font-size:11px;color:#bbb}
.badge{top:10px;width:88px;height:30px;border-radius:3px;background:#555;border:1px solid #777}
</style>
</head>
<body>
<div class="abs topline"></div>
<header class="abs header">
  <div class="abs brand"><span class="brand-dot"></span><span class="brand-name">vexlo</span></div>
  <nav class="abs nav"><a class="active">Home</a><a>About</a><a>Services</a><a>Portfolio</a><a>News</a><a>Contact</a></nav>
</header>

<section class="abs hero">
  <div class="abs hero-art" role="img" aria-label="Product shot of a white smartphone beside a green robot figure"></div>
  <h1 class="abs">Welcome to our site</h1>
  <div class="abs rule" style="top:120px"></div>
  <p class="abs">Mauris quis risus et risus posuere lacinia. Proin pellentesque cursus ipsum a convallis. Maecenas at dui sagittis felis porta ultrices. Vivamus vel mauris egestas purus dignissim facilisis. Nulla tristique est a eros ultricies ullam corper. Maecenas quis mi ligula. Vivamus accumsan massa vel magna bibendum in blandit metus tristique.</p>
  <div class="abs rule" style="top:242px"></div>
  <div class="abs pill">View more</div>
  <div class="abs arrows">
    <span><svg width="6" height="8"><path d="M5 0L1 4l4 4" stroke="#fff" stroke-width="1.8" fill="none"/></svg></span>
    <span><svg width="6" height="8"><path d="M1 0l4 4-4 4" stroke="#fff" stroke-width="1.8" fill="none"/></svg></span>
  </div>
</section>

<section class="abs about">
  <h2 class="abs">About Vexlo</h2>
  <p class="abs">Vivamus at erat sed diam suscipit fringilla. Nullam ornare auctor neque quis commodo. Proin elementum sodales nulla, vitae faucibus velit iaculis a. Donec ligula augue, vulputate a placerat nec, varius sed ligula. Vivamus tellus lectus, porta vitae aliquam et, auctor non diam. Nunc metus diam, gravida non dictum vel, mattis a ante. Aenean eget odio ac neque consequat dapibus id sit amet massa. Suspendisse rutrum rhoncus eros, eu imperdiet leo laoreet quis. Nullam aliquam orci id neque condimentum eu pellentesque neque blandit.</p>
  <div class="abs frame"><div role="img" aria-label="Photo of a hand holding a smartphone on a brick pavement" style="background:linear-gradient(90deg,#c9b2a6,#a58a7d 45%,#3c4048 60%,#c08a70)"></div></div>
</section>
<div class="abs divider"></div>

<div class="abs col" style="left:75px">
  <h3>Most Recent Job</h3><span class="go"></span>
  <div class="frame"><div role="img" aria-label="Collage of colourful app icons on a dark background" style="background:linear-gradient(120deg,#6d5a3a,#2a2a2a 50%,#333)"></div></div>
  <p>Sed dui lacus, consectetur eu congue in, luctus ut ante. Vivamus tincidunt tempor enim, non pretium odio molestie sedvel nunc ornare aliquam.</p>
  <div class="btn" style="margin-top:8px">View more</div>
</div>
<div class="abs col" style="left:366px">
  <h3>Most Recent News</h3><span class="go"></span>
  <div class="frame"><div role="img" aria-label="Illustration of a green robot surrounded by app icons" style="background:radial-gradient(circle,#9ccf4a 0,#e6eee0 35%,#f2f2f2)"></div></div>
  <p>Sed dui lacus, consectetur eu congue in, luctus ut ante. Vivamus tincidunt tempor enim, non pretium odio molestie sedvel nunc ornare aliquam.</p>
  <div class="btn" style="margin-top:8px">View more</div>
</div>
<div class="abs col" style="left:657px;width:256px">
  <h3>Our Services</h3>
  <ul class="services">
    <li><svg width="14" height="10"><path d="M0 3h8V0l6 5-6 5V7H0z" fill="#5a9de6"/></svg>Mauris aliquet dapibus</li>
    <li><svg width="14" height="10"><path d="M0 3h8V0l6 5-6 5V7H0z" fill="#5a9de6"/></svg>Nam ultrices, felis at aliquam</li>
    <li><svg width="14" height="10"><path d="M0 3h8V0l6 5-6 5V7H0z" fill="#5a9de6"/></svg>Aenean vitae massa</li>
    <li><svg width="14" height="10"><path d="M0 3h8V0l6 5-6 5V7H0z" fill="#5a9de6"/></svg>Mauris quis risus et risus posuere</li>
    <li><svg width="14" height="10"><path d="M0 3h8V0l6 5-6 5V7H0z" fill="#5a9de6"/></svg>Proin elementum sodales nulla, vitae</li>
    <li><svg width="14" height="10"><path d="M0 3h8V0l6 5-6 5V7H0z" fill="#5a9de6"/></svg>Vestibulum sed purusnec</li>
    <li><svg width="14" height="10"><path d="M0 3h8V0l6 5-6 5V7H0z" fill="#5a9de6"/></svg>Quisque adipiscing vitlana</li>
  </ul>
  <div class="btn" style="margin-top:1px">View more</div>
</div>

<footer class="abs footer">
  <h4 class="abs" style="left:75px;top:20px">Quick Links</h4>
  <ul class="abs links" style="left:78px"><li>Nam faucibus</li><li>Proin dignissim turpis</li><li>Duis posuere</li><li>Vivamus nec tortor</li><li>Phasellus malesuada</li><li>Etiam sed</li></ul>
  <ul class="abs links" style="left:250px"><li>Nam faucibus</li><li>Proin dignissim turpis</li><li>Duis posuere</li><li>Vivamus nec tortor</li><li>Phasellus malesuada</li><li>Etiam sed</li></ul>
  <ul class="abs links" style="left:411px"><li>Nam faucibus</li><li>Proin dignissim turpis</li><li>Duis posuere</li><li>Vivamus nec tortor</li><li>Phasellus malesuada</li><li>Etiam sed</li></ul>
  <ul class="abs links" style="left:583px"><li>Nam faucibus</li><li>Proin dignissim turpis</li><li>Duis posuere</li><li>Vivamus nec tortor</li><li>Phasellus malesuada</li><li>Etiam sed</li></ul>
  <h4 class="abs" style="left:743px;top:20px">Connect with us</h4>
  <ul class="abs social">
    <li><i></i><span>Join with us on<b>Kinnect</b></span></li>
    <li><i style="background:#3ba7df"></i><span>Follow us on<b>Chirply</b></span></li>
    <li><i style="background:#2a6fa8"></i><span>Share on<b>Proflink</b></span></li>
    <li><i style="background:#c9c9c9"></i><span>Watch on<b>Vidstream</b></span></li>
  </ul>
</footer>

<div class="abs bar">
  <p class="abs">Copyright &nbsp;© &nbsp;2013 &nbsp;&nbsp;www.vexlo.example &nbsp;&nbsp;All rights reserved.</p>
  <div class="abs badge" style="left:725px"></div>
  <div class="abs badge" style="left:821px"></div>
</div>
</body>
</html>
```